Book cover for LM

Design cover for a book of gratitude and inspiration.
Book trim size will be 6.5 x 6.5 inches, or 8 x 8 inches, hardcover, 96 pages
Title: Lantern Meadows
Subtitle: A Book of Gratitude and Inspiration
Author: Gus Halverd

```html
<!DOCTYPE html>
<html lang="en">
<head>
<meta charset="utf-8">
<title>Lantern Meadows — Book Cover</title>
<link href="https://fonts.googleapis.com/css2?family=Bebas+Neue&family=Montserrat:wght@500;700&display=swap" rel="stylesheet">
<style>
  :root {
    --cover-bg: #02484c;
    --botanical-mid: #3f7b7a;
    --botanical-soft: #2a6466;
    --title-pink: #ff9a9a;
    --text-white: #ffffff;
  }
  html, body {
    margin: 0;
    padding: 0;
    width: 1200px;
    height: 1200px;
    overflow: hidden;
    background: var(--cover-bg);
  }
  .cover {
    position: relative;
    width: 1200px;
    height: 1200px;
    background: var(--cover-bg);
    overflow: hidden;
  }
  .botanical-art {
    position: absolute;
    left: 170px;
    top: 25px;
    width: 860px;
    height: 1160px;
    border-radius: 46% 46% 40% 40% / 30% 30% 28% 28%;
    background: radial-gradient(ellipse at 50% 50%,
      var(--botanical-mid) 0%,
      var(--botanical-soft) 55%,
      rgba(2, 72, 76, 0) 78%);
  }
  .title {
    position: absolute;
    left: 0;
    top: 0;
    width: 1200px;
    height: 1200px;
    margin: 0;
    font-weight: 400;
  }
  .title-art {
    display: block;
    width: 1200px;
    height: 1200px;
  }
  .title-line {
    font-family: "Bebas Neue", "Oswald", sans-serif;
    fill: var(--title-pink);
  }
  .title-line--first { font-size: 283px; }
  .title-line--second { font-size: 386px; }
  .subtitle {
    position: absolute;
    left: 0;
    width: 1220px;
    margin: 0;
    top: 830px;
    text-align: center;
    font-family: "Montserrat", sans-serif;
    font-weight: 500;
    font-size: 58px;
    line-height: 68px;
    letter-spacing: 0.02em;
    color: var(--text-white);
    text-transform: uppercase;
  }
  .author {
    position: absolute;
    left: 0;
    width: 1202px;
    margin: 0;
    top: 1070px;
    text-align: center;
    font-family: "Montserrat", sans-serif;
    font-weight: 700;
    font-size: 76px;
    line-height: 1;
    letter-spacing: 0.01em;
    color: var(--text-white);
    text-transform: uppercase;
  }
</style>
</head>
<body>
  <main class="cover">
    <div class="botanical-art" role="img" aria-label="Hand-drawn botanical illustration of leaves, vines, buds and blossoms in muted teal"></div>
    <h1 class="title">
      <svg class="title-art" viewBox="0 0 1200 1200" aria-label="Lantern Meadows">
        <text class="title-line title-line--first" x="83" y="468" textLength="1034" lengthAdjust="spacing">LANTERN</text>
        <text class="title-line title-line--second" x="83" y="756" textLength="1030" lengthAdjust="spacingAndGlyphs">MEADOWS</text>
      </svg>
    </h1>
    <p class="subtitle">A Book of Gratitude<br>and Inspiration</p>
    <p class="author">Gus Halverd</p>
  </main>
</body>
</html>
```